Outdoor cooking competition needs 10yr celebration poster

We are a fundraising event held every year in a tiny outback town in australia. the cooking competition is a 'camp oven' themed competition. people are required to cook in the ground in coals with a camp oven (dutch oven).
the event is celebrating ten years and needs a new flashy poster to let people know.

the event raises much needed funds for "the Sunward Air Medic" a a donation funded scheme which flys doctors and patients to and from remote australia.

The EMBER DUST FEAST is held annually in the tiny town of Blinman in the northern Ridgeline Tours. The main street of the town, camp ground, and surrounding area have been landscaped to suit the competitions purpose. A giant ‘creek bed’ kitchen is created with tones of rocks and gravel transforming the street and adjacent hill side. The picturesque and historic Quarrow Hotel with its verandahs and characteristic front bar, will form a focus, the remaining street precinct will be the venue for exhibitions, wine tasting, food outlets, trade displays, demonstrations and live music.

Payment now GARAUNTEED!

• Must display our logo
dates and venues
10 year celebration
room to add sponsorship logos

```html
<!DOCTYPE html>
<html lang="en">
<head>
<meta charset="utf-8">
<title>Ember Dust Feast – 10 Year Celebration Poster</title>
<link rel="stylesheet" href="https://fonts.googleapis.com/css2?family=Roboto+Condensed:wght@700&family=Arimo:wght@700&family=IM+Fell+English&display=swap">
<style>
  :root {
    --page: #ffffff;
    --board: #f1f1f1;
    --parchment-light: #e4cf9e;
    --parchment: #cfb07a;
    --parchment-dark: #a9834b;
    --art-tone: #b89664;
    --ink: #1a120c;
    --ribbon: #ead6a6;
    --ribbon-ink: #4a2a12;
    --plank: #5a2e1a;
    --plank-text: #f6ece0;
    --footer: #0c0c0c;
    --footer-text: #e29a2b;
    --sponsor-brown: #a85a32;
    --sponsor-red: #d81f26;
    --white: #ffffff;
  }
  * { box-sizing: border-box; margin: 0; padding: 0; }
  html, body { width: 1200px; height: 900px; overflow: hidden; background: var(--page); }
  .canvas { position: relative; width: 1200px; height: 900px; }
  .board {
    position: absolute; left: 22px; top: 28px; width: 1156px; height: 844px;
    background: linear-gradient(90deg, #e9e9e9, var(--board) 40%, #fafafa);
    border-radius: 16px;
  }
  .poster {
    position: absolute; left: 123px; top: 28px; width: 599px; height: 848px;
    background: var(--footer);
    box-shadow: 2px 3px 8px rgba(0,0,0,.45);
    overflow: hidden;
  }
  .parchment {
    position: absolute; left: 0; top: 0; width: 599px; height: 678px;
    background: radial-gradient(ellipse at 45% 40%, var(--parchment-light), var(--parchment) 60%, var(--parchment-dark));
  }
  .ribbon {
    position: absolute; left: 14px; top: 32px; width: 360px; height: 52px;
    background: var(--ribbon);
    transform: rotate(-9deg);
    box-shadow: 0 2px 4px rgba(0,0,0,.3);
    font-family: "IM Fell English", serif; font-size: 33px; color: var(--ribbon-ink);
    display: flex; align-items: center; justify-content: center;
  }
  .headline {
    position: absolute; left: 0; width: 599px; text-align: center; white-space: nowrap;
    font-family: "Roboto Condensed", sans-serif; font-weight: 700; color: var(--ink);
  }
  .venue { top: 100px; font-size: 56px; letter-spacing: 1.5px; }
  .event-type { top: 154px; font-size: 27px; letter-spacing: .5px; }
  .dates { top: 186px; font-size: 42px; }
  .dates sup { font-size: 22px; vertical-align: 15px; }
  .event-name {
    position: absolute; left: 112px; top: 242px; width: 242px; height: 286px;
    background: var(--white); border: 5px solid var(--ink);
    font-family: "Roboto Condensed", sans-serif; font-weight: 700; color: var(--ink);
    font-size: 78px; line-height: 92px; text-align: center;
  }
  .camp-oven-art {
    position: absolute; left: 62px; top: 446px; width: 312px; height: 232px;
    background: linear-gradient(180deg, var(--parchment) 0%, var(--art-tone) 100%);
    border-radius: 6px;
  }
  .prize {
    position: absolute; left: 395px; top: 238px; width: 170px; text-align: center;
    font-family: "Arimo", sans-serif; font-weight: 700; color: var(--ink);
  }
  .prize .small { font-size: 24px; line-height: 28px; }
  .prize .amount { font-size: 38px; line-height: 44px; }
  .beneficiary {
    position: absolute; left: 395px; top: 354px; width: 170px; text-align: center;
    font-family: "Arimo", sans-serif; font-weight: 700; font-size: 17px; line-height: 25px; color: var(--ink);
  }
  .signpost {
    position: absolute; left: 388px; top: 468px; width: 188px; height: 210px;
    background: var(--plank); border-radius: 3px;
    padding-top: 6px;
  }
  .signpost-item {
    height: 26.5px; text-align: center;
    font-family: "Arimo", sans-serif; font-weight: 700; font-size: 17px; line-height: 26.5px;
    color: var(--plank-text); letter-spacing: .5px;
  }
  .web-band {
    position: absolute; left: 0; top: 678px; width: 599px; height: 40px; background: var(--white);
    font-family: "Arimo", sans-serif; font-weight: 700; font-size: 31px; color: var(--ink);
    text-align: center; line-height: 40px; letter-spacing: .5px;
  }
  .sponsor {
    position: absolute; top: 737px; height: 73px; white-space: nowrap;
    font-family: "Roboto Condensed", sans-serif; font-weight: 700;
    display: flex; align-items: center; justify-content: center; text-align: center;
  }
  .sponsor-haldane { left: 12px; width: 60px; background: var(--sponsor-brown); color: var(--white); font-size: 12px; }
  .sponsor-motors { left: 78px; width: 220px; background: var(--white); border: 5px solid var(--sponsor-red); color: var(--sponsor-red); font-size: 27px; }
  .sponsor-hotel { left: 307px; width: 141px; background: var(--sponsor-brown); color: var(--white); font-size: 16px; }
  .sponsor-brewing { left: 455px; width: 79px; height: 56px; background: var(--white); color: var(--sponsor-red); font-size: 13px; line-height: 15px; white-space: normal; }
  .sponsor-tours { left: 540px; width: 49px; background: var(--white); color: var(--ink); font-size: 10px; line-height: 12px; white-space: normal; }
  .contact {
    position: absolute; left: 0; top: 822px; width: 599px; text-align: center;
    font-family: "Arimo", sans-serif; font-weight: 700; font-size: 9px; color: var(--footer-text);
  }
  .logo-card {
    position: absolute; left: 847px; top: 484px; width: 316px; height: 382px;
    background: var(--white); border: 7px solid var(--ink);
    font-family: "Roboto Condensed", sans-serif; font-weight: 700; color: var(--ink);
    font-size: 98px; line-height: 122px; text-align: center;
    display: flex; flex-direction: column; justify-content: center;
  }
</style>
</head>
<body>
<div class="canvas">
  <div class="board"></div>

  <div class="poster">
    <div class="parchment" role="img" aria-label="Aged, torn parchment paper texture with burnt edges"></div>

    <div class="ribbon">10 Year Celebration</div>

    <div class="headline venue">QUARROW HOTEL</div>
    <div class="headline event-type">CAMP OVEN COOK OFF</div>
    <div class="headline dates">SEPTEMBER 29<sup>TH</sup> &amp; 30<sup>TH</sup> 2012</div>

    <div class="camp-oven-art" role="img" aria-label="Sketched camp oven pot over coals with steam rising"></div>

    <div class="event-name">EMBER<br>DUST<br>FEAST</div>

    <div class="prize">
      <div class="small">up to</div>
      <div class="amount">$5000</div>
      <div class="small">in prizes</div>
    </div>

    <div class="beneficiary">All proceeds<br>To the<br>Sunward Air<br>Medic Service</div>

    <div class="signpost" role="img" aria-label="Wooden signpost listing event attractions">
      <div class="signpost-item">exhibitions</div>
      <div class="signpost-item">wine tasting</div>
      <div class="signpost-item">food outlets</div>
      <div class="signpost-item">trade displays</div>
      <div class="signpost-item">demonstrations</div>
      <div class="signpost-item">live music.</div>
    </div>

    <div class="web-band">www.emberdustfeast.com.au</div>

    <div class="sponsor sponsor-haldane">HALDANE</div>
    <div class="sponsor sponsor-motors">MARROW MOTORS</div>
    <div class="sponsor sponsor-hotel">QUARROW HOTEL</div>
    <div class="sponsor sponsor-brewing">RED GUM BREWING</div>
    <div class="sponsor sponsor-tours">RIDGELINE TOURS</div>

    <div class="contact">FOR FURTHER INFORMATION PH: 08 8600 2417</div>
  </div>

  <div class="logo-card">
    <span>EMBER</span><span>DUST</span><span>FEAST</span>
  </div>
</div>
</body>
</html>
```